Tri-fold flyer for Managed Services IT company

We need a tri-fold flyer design for our Managed Services IT company. Our website is here: https://pelicanfjordit.net. While we don't have to match our website we do want to incorporate the logo in the flyer. We would like a flyer that is *very* easy and quick to read/skim over and convey our message. Something like these:

https://www.artkestrel.com/design/58203917

https://47sketchyard.com/postcard-flyer-design/contests/create-lead-generating-flyer-postcard-managed-services-company-815243

http://www.marbleoaksystems.com/managed-services-no-cost-one-month/

Target Market(s)

Business to business IT services

Industry/Entity Type

It Service

Font styles to use
Serif
Sans Serif

Requirements
Must have
• *very* easy and quick to read/skim over and convey our message
Should not have
• verbose, lots of text

```html
<!DOCTYPE html>
<html lang="en">
<head>
<meta charset="utf-8">
<title>Pelican Fjord IT — Our Services Tri-fold</title>
<link rel="stylesheet" href="https://fonts.googleapis.com/css2?family=Ubuntu:wght@400;500&display=swap">
<style>
  :root {
    --page-bg: #e8eaee;
    --navy-deep: #0b1430;
    --navy: #14285a;
    --blue-glow: #2d6fd0;
    --crimson: #b3163f;
    --crimson-dark: #8c1033;
    --red: #e21b2c;
    --white: #ffffff;
    --text: #eef2fb;
  }
  * { box-sizing: border-box; margin: 0; padding: 0; }
  html, body {
    width: 815px; height: 1200px; overflow: hidden;
    background: var(--page-bg);
    font-family: "Ubuntu", sans-serif;
  }
  .flyer {
    position: absolute; left: 0; top: 317px;
    width: 815px; height: 565px;
    overflow: hidden;
    color: var(--text);
  }
  .flyer-backdrop {
    position: absolute; inset: 0;
    background:
      radial-gradient(ellipse at 55% 45%, rgba(80,150,240,.55) 0%, rgba(45,111,208,.25) 30%, transparent 60%),
      radial-gradient(ellipse at 85% 80%, rgba(60,130,230,.4) 0%, transparent 45%),
      linear-gradient(180deg, var(--navy) 0%, var(--navy-deep) 100%);
  }
  .panel-shade {
    position: absolute; top: 0; bottom: 0; width: 272px;
    background: rgba(5,10,30,.28);
  }
  .panel-shade.left { left: 0; }
  .panel-shade.right { right: 0; }
  .top-band {
    position: absolute; left: 0; right: 0; top: 0; height: 28px;
    background: linear-gradient(180deg, var(--crimson) 0%, var(--crimson-dark) 100%);
  }
  .band-title {
    position: absolute; left: 265px; top: 0; width: 264px; height: 38px;
    background: var(--red);
    color: var(--white);
    font-size: 22px; font-weight: 500; letter-spacing: .5px;
    display: flex; align-items: center; justify-content: center;
  }
  .service {
    position: absolute; width: 250px;
  }
  .service-icon {
    display: block; margin: 0 auto; height: 50px; width: 60px;
  }
  .service-title {
    margin-top: 14px;
    text-align: center; font-size: 16px; font-weight: 400; color: var(--white);
    position: relative; padding-bottom: 3px;
  }
  .service-title::after {
    content: ""; position: absolute; left: 50%; bottom: -2px;
    width: 150px; height: 3px; margin-left: -75px;
    background: var(--red);
  }
  .service-text {
    margin-top: 9px; font-size: 9.6px; line-height: 1.38; color: var(--text);
  }
  .col-1 { left: 14px; }
  .col-2 { left: 283px; }
  .col-3 { left: 553px; }
  .row-1 { top: 82px; }
  .row-2 { top: 310px; }
</style>
</head>
<body>
<main class="flyer">
  <div class="flyer-backdrop" role="img" aria-label="Glowing blue network of connected points and lines on a dark navy background"></div>
  <div class="panel-shade left"></div>
  <div class="panel-shade right"></div>

  <div class="top-band"></div>
  <h1 class="band-title">OUR SERVICES</h1>

  <section class="service col-1 row-1">
    <svg class="service-icon" viewBox="0 0 60 50" fill="none" stroke="#fff" stroke-width="2">
      <rect x="12" y="18" width="36" height="22" rx="1"/>
      <path d="M24 46h12M30 40v6"/>
      <path d="M22 18V8M30 18V4M38 18V8"/>
      <circle cx="22" cy="6" r="2"/><circle cx="30" cy="2.5" r="1.8"/><circle cx="38" cy="6" r="2"/>
    </svg>
    <h2 class="service-title">Managed IT Services</h2>
    <p class="service-text">Computer and network support for DC Metro small and midsized businesses. Downtime is a profit killer. At Pelican Fjord IT, we recognize that in order to maximize profitability, your company's IT has to be up-and-running. That's why we provide comprehensive IT support to small and midsized Businesses in the DC Metro area. Ou The legal profession has always relied</p>
  </section>

  <section class="service col-2 row-1">
    <svg class="service-icon" viewBox="0 0 60 50" fill="#fff">
      <circle cx="24" cy="26" r="11"/>
      <g stroke="#fff" stroke-width="5">
        <path d="M24 11v30M9 26h30M13.5 15.5l21 21M34.5 15.5l-21 21"/>
      </g>
      <circle cx="24" cy="26" r="4" fill="#14285a"/>
      <circle cx="43" cy="12" r="6"/>
      <g stroke="#fff" stroke-width="3"><path d="M43 3v18M34 12h18M37 6l12 12M49 6L37 18"/></g>
      <circle cx="43" cy="12" r="2.2" fill="#14285a"/>
      <circle cx="44" cy="38" r="6"/>
      <g stroke="#fff" stroke-width="3"><path d="M44 29v18M35 38h18M38 32l12 12M50 32L38 44"/></g>
      <circle cx="44" cy="38" r="2.2" fill="#14285a"/>
    </svg>
    <h2 class="service-title">Software Services</h2>
    <p class="service-text">For small and midsized businesses, the Quillstone Office productivity suite is a staple in your software cupboard. Consider how much you have paid for each software license. How would you feel about spending a fraction of the cost for the entire Quillstone Office</p>
  </section>

  <section class="service col-3 row-1">
    <svg class="service-icon" viewBox="0 0 60 50" fill="#fff" stroke="#fff" stroke-width="2">
      <path d="M30 6v38M20 46h20M12 12h36" fill="none"/>
      <circle cx="30" cy="6" r="3"/>
      <path d="M12 12L5 28M12 12l7 16M48 12l-7 16M48 12l7 16" fill="none"/>
      <path d="M4 28h16a8 6 0 0 1-16 0zM40 28h16a8 6 0 0 1-16 0z"/>
    </svg>
    <h2 class="service-title">Software Services</h2>
    <p class="service-text">heavily on the newest technologies. Pelican Fjord IT can provide your practice with dynamic options that can save you money. It's a fact that lawyers are at the center of many important decisions. As with many other economic sectors nowadays, technology is .</p>
  </section>

  <section class="service col-1 row-2">
    <svg class="service-icon" viewBox="0 0 60 50">
      <path d="M30 3l18 7v14c0 12-8 20-18 24C20 44 12 36 12 24V10z" fill="#fff"/>
      <rect x="23" y="24" width="14" height="11" rx="1" fill="#14285a"/>
      <path d="M25.5 24v-4a4.5 4.5 0 0 1 9 0v4" fill="none" stroke="#14285a" stroke-width="2.2"/>
    </svg>
    <h2 class="service-title">Security Services</h2>
    <p class="service-text">Eliminate wasted time and money by managing your security from one location. Standard point-of-service security solutions are highly difficult to institute, update, and manage. This can lead to complex operations and an increase to overhead cost. Pelican Fjord IT is able to help you eliminate these issues with an All-In-One Security (UTM).</p>
  </section>

  <section class="service col-2 row-2">
    <svg class="service-icon" viewBox="0 0 60 50" fill="none" stroke="#fff" stroke-width="2.5">
      <path d="M15 42a10 10 0 0 1-1-20 14 14 0 0 1 27-4 11 11 0 0 1 5 24z"/>
    </svg>
    <h2 class="service-title">Data Services</h2>
    <p class="service-text">t's important to implement a data recovery solution as part of a concise business continuity plan. There once was a time where companies required steel filing cabinets to store information. That time is long gone. Today, most of the documents your employees rely on to make your business run properly are proof vaults, and off-site filing</p>
  </section>

  <section class="service col-3 row-2">
    <svg class="service-icon" viewBox="0 0 60 50" fill="#fff">
      <circle cx="22" cy="10" r="7"/>
      <path d="M8 44c0-14 6-22 14-22s14 8 14 22z"/>
      <path d="M22 22l-2 5 2 10 2-10z" fill="#14285a"/>
      <rect x="38" y="34" width="4" height="10"/>
      <rect x="44" y="28" width="4" height="16"/>
      <rect x="50" y="22" width="4" height="22"/>
      <path d="M37 28l8-9 5 3 6-8" fill="none" stroke="#fff" stroke-width="2"/>
    </svg>
    <h2 class="service-title">Software Services</h2>
    <p class="service-text">Voice over Internet Protocol is easy to use, cost-effective, and flexible. Having a capable phone system is essential for a growing business. Fully-featured VoIP solutions from Pelican Fjord IT are able to offer your business major cost-benefits since it utilizes your Internet connection for all of your organization's communication needs.</p>
  </section>
</main>
</body>
</html>
```